QMB Vane Works

- Brochure design

Target Market(s)

Granite and Quartz

Font styles to use
Sans Serif

Colors

Designer to choose colors to be used in the design.

Requirements
Must have
• I post the instruction file below
Nice to have
Should not have

```html
<!DOCTYPE html>
<html lang="en">
<head>
<meta charset="utf-8">
<title>QMB Vane Works – Product Catalog Brochure</title>
<link rel="stylesheet" href="https://fonts.googleapis.com/css2?family=Open+Sans:wght@400;600;700&family=Oswald:wght@400;700&family=Montserrat:wght@400;700;800&family=Cinzel:wght@400&family=Lora:ital@1&display=swap">
<style>
  :root {
    --stage: #3b3b3e;
    --salmon: #d9806a;
    --salmon-deep: #c96d57;
    --slate: #4b4c58;
    --slate-dark: #3a3b45;
    --paper: #ffffff;
    --ink: #3d3d44;
    --label: #e9e9ec;
  }
  * { box-sizing: border-box; margin: 0; padding: 0; }
  html, body { width: 895px; height: 1200px; overflow: hidden; }
  body { background: var(--stage); font-family: "Open Sans", sans-serif; position: relative; }

  .spread { position: absolute; left: 47px; width: 800px; height: 520px; display: flex; box-shadow: 0 10px 30px rgba(0,0,0,.45); }
  .spread--outside { top: 36px; }
  .spread--inside { top: 630px; }
  .page { position: relative; width: 400px; height: 520px; overflow: hidden; }

  .spread-label { position: absolute; right: 48px; color: var(--label); font-family: "Montserrat", sans-serif; font-weight: 400; font-size: 15px; letter-spacing: .3px; }
  .spread-label--outside { top: 578px; }
  .spread-label--inside { top: 1168px; }

  /* Back cover */
  .back-cover { background: var(--slate); color: var(--paper); }
  .back-cover__photo { position: absolute; inset: 0; background: linear-gradient(160deg, #5b5c68 0%, #4b4c58 45%, #43444f 100%); opacity: .9; }
  .back-cover__brand { position: absolute; left: 0; right: 0; top: 330px; text-align: center; font-family: "Open Sans", sans-serif; font-weight: 600; font-size: 26px; }
  .back-cover__tagline { position: absolute; left: 0; right: 0; top: 368px; text-align: center; font-family: "Cinzel", serif; font-size: 15px; letter-spacing: 2px; color: #e3e3e8; }
  .contact-row { position: absolute; left: 30px; right: 30px; top: 418px; height: 40px; }
  .contact-row svg { position: absolute; left: 0; top: 0; }
  .contact { position: absolute; top: 30px; font-size: 7.5px; color: #e6e6ea; white-space: nowrap; }
  .category-list { position: absolute; left: 0; right: 0; bottom: 22px; text-align: center; font-size: 8px; font-weight: 700; color: #f0f0f2; }
  .category-list span::before { content: "•"; color: var(--salmon); margin: 0 5px; }

  /* Front cover */
  .front-cover { background: var(--salmon); padding: 12px 14px 12px; display: flex; flex-direction: column; }
  .front-cover__inner { background: var(--paper); flex: 1; display: flex; flex-direction: column; }
  .front-cover__head { height: 98px; text-align: center; padding-top: 12px; }
  .front-cover__brand { font-family: "Open Sans", sans-serif; font-weight: 600; font-size: 22px; color: var(--ink); }
  .front-cover__company { font-family: "Montserrat", sans-serif; font-weight: 800; font-size: 15px; color: var(--salmon); margin-top: 2px; }
  .front-cover__tagline { font-family: "Lora", serif; font-style: italic; font-size: 11px; color: var(--ink); margin-top: 3px; }
  .front-cover__photo { height: 200px; background: linear-gradient(180deg, #eef1f2 0%, #d7dcd8 55%, #b9b8a6 100%); }
  .front-cover__band { background: var(--salmon); height: 128px; padding: 26px 18px 0; color: var(--paper); font-family: "Oswald", sans-serif; }
  .front-cover__company-line { font-size: 22px; font-weight: 400; line-height: 1.1; white-space: nowrap; }
  .front-cover__company-line b { font-weight: 700; }
  .front-cover__title { font-size: 40px; font-weight: 700; line-height: 1.2; letter-spacing: .5px; white-space: nowrap; }
  .front-cover__strip { background: var(--slate); height: 20px; display: flex; align-items: center; justify-content: center; font-size: 7.5px; font-weight: 700; color: var(--paper); }
  .front-cover__strip span::before { content: "•"; color: var(--salmon); margin: 0 5px; }
  .front-cover__web { flex: 1; display: flex; align-items: center; justify-content: center; font-size: 9px; letter-spacing: 3px; color: var(--ink); }

  /* Inside pages */
  .inside-page { background: var(--paper); }
  .page-header { position: absolute; left: 0; right: 0; top: 0; height: 68px; background: var(--salmon); color: var(--paper); font-family: "Montserrat", sans-serif; font-weight: 800; font-size: 24px; display: flex; align-items: flex-end; padding-bottom: 12px; white-space: nowrap; }
  .page-header--left { justify-content: flex-end; padding-right: 10px; }
  .page-header--right { padding-left: 10px; }
  .partner-name { position: absolute; top: 22px; font-family: "Open Sans", sans-serif; font-weight: 700; font-size: 11px; color: var(--paper); display: flex; align-items: center; gap: 5px; }
  .partner-name i { width: 12px; height: 12px; border-radius: 50%; background: var(--paper); display: inline-block; }
  .partner-name--left { left: 14px; }
  .partner-name--right { right: 14px; }

  .photo-gray { position: absolute; background: linear-gradient(170deg, #d6d6d8 0%, #a9a9ad 45%, #5e5f66 100%); }
  .inside-page--granite .photo-gray { left: 0; top: 68px; width: 400px; height: 402px; }
  .inside-page--quartz .photo-gray { left: 150px; top: 68px; width: 250px; height: 392px; }

  .text-column { position: absolute; top: 68px; color: var(--paper); padding: 18px 16px; font-size: 8.5px; line-height: 1.4; }
  .text-column h2 { font-family: "Montserrat", sans-serif; font-weight: 800; font-size: 13px; margin-bottom: 8px; letter-spacing: .5px; }
  .text-column p + p { margin-top: 14px; }
  .text-column--granite { left: 200px; width: 186px; height: 402px; background: var(--salmon); }
  .text-column--quartz { left: 0; width: 150px; height: 392px; background: var(--slate); }

  .page-number { position: absolute; width: 22px; height: 22px; border: 1.5px solid var(--salmon); border-radius: 50%; color: var(--salmon); font-size: 8px; font-weight: 700; display: flex; align-items: center; justify-content: center; }
  .inside-page--granite .page-number { left: 22px; bottom: 16px; }
  .inside-page--quartz .page-number { right: 22px; bottom: 30px; }
  .page-rule { position: absolute; left: 0; bottom: 0; }
</style>
</head>
<body>

<section class="spread spread--outside" aria-label="Outside spread">
  <article class="page back-cover">
    <div class="back-cover__photo" role="img" aria-label="Faded kitchen interior with pendant lights under a slate overlay"></div>
    <div class="back-cover__brand">Vane Works</div>
    <div class="back-cover__tagline">PREMIUM QUALITY</div>
    <div class="contact-row">
      <svg width="340" height="30" viewBox="0 0 340 30" aria-hidden="true">
        <line x1="0" y1="14" x2="340" y2="14" stroke="#d9806a" stroke-width="1"/>
        <g fill="none" stroke="#d9806a" stroke-width="1.4">
          <circle cx="40" cy="14" r="11"/><circle cx="170" cy="14" r="11"/><circle cx="300" cy="14" r="11"/>
        </g>
        <g fill="none" stroke="#d9806a" stroke-width="1.3">
          <path d="M34 15 L40 9 L46 15 M36 14 V19 H44 V14"/>
          <path d="M165 9 q-1 6 5 11 l2 -2 -2 -2 -1 1 q-2 -2 -2 -4 l1 -1 -2 -2z"/>
          <circle cx="300" cy="14" r="5.5"/><path d="M294.5 14 H305.5 M300 8.5 q-3 5.5 0 11 q3 -5.5 0 -11"/>
        </g>
      </svg>
      <span class="contact" style="left:0">4870 Marlow Court, Denton, TX 76201</span>
      <span class="contact" style="left:145px">555-014-2287</span>
      <span class="contact" style="left:252px">www.qmbvaneworks.com</span>
    </div>
    <div class="category-list"><span>Natural Stone</span><span>Pre-Fabricate Slabs</span><span>Natural Stone</span><span>Granite</span><span>Quartz</span></div>
  </article>

  <article class="page front-cover">
    <div class="front-cover__inner">
      <header class="front-cover__head">
        <div class="front-cover__brand">Vane Works</div>
        <div class="front-cover__company">QMB Vane Works, Inc</div>
        <div class="front-cover__tagline">Naturally Beautiful, Premium Quality</div>
      </header>
      <div class="front-cover__photo" role="img" aria-label="Bright white kitchen with marble island, pendant lamps, potted flowers and tall windows"></div>
      <div class="front-cover__band">
        <div class="front-cover__company-line"><b>QMB</b> VANE WORKS, INC</div>
        <div class="front-cover__title">PRODUCT CATALOG</div>
      </div>
      <div class="front-cover__strip"><span>Natural Stone</span><span>Pre-Fabricate Slabs</span><span>Natural Stone</span><span>Granite</span><span>Quartz</span></div>
      <div class="front-cover__web">www.qmbvaneworks.com</div>
    </div>
  </article>
</section>
<div class="spread-label spread-label--outside">Outside</div>

<section class="spread spread--inside" aria-label="Inside pages 1 and 2">
  <article class="page inside-page inside-page--granite">
    <header class="page-header page-header--left">Comparison Between</header>
    <div class="partner-name partner-name--left"><i></i>Slabline</div>
    <div class="photo-gray" role="img" aria-label="Black and white kitchen with dark wood island, granite top and pendant lamp"></div>
    <div class="text-column text-column--granite">
      <h2>GRANITE</h2>
      <p>Granite is a natural stone formed deep underground, giving every slab its own veining, depth and colour. It resists heat and scratches and lasts for decades in busy kitchens.</p>
      <p>Each slab is cut, polished and sealed in our shop before it reaches your home. A yearly reseal keeps the surface bright and protects it from stains and spills.</p>
    </div>
    <svg class="page-rule" width="400" height="50" viewBox="0 0 400 50" aria-hidden="true"><line x1="40" y1="40" x2="400" y2="8" stroke="#d9806a" stroke-width="1"/></svg>
    <div class="page-number">01</div>
  </article>

  <article class="page inside-page inside-page--quartz">
    <header class="page-header page-header--right">GRANITE &amp; QUARTE</header>
    <div class="partner-name partner-name--right"><i></i>Crestmark</div>
    <div class="text-column text-column--quartz">
      <h2>QUARTE</h2>
      <p>Quartz is an engineered surface made from crushed stone and resin. It offers a steady pattern, a wide range of colours and a non-porous finish that needs no sealing.</p>
      <p>It stands up to daily wear, cleans with mild soap and water, and keeps its even look for years. Ask our team to compare samples side by side.</p>
    </div>
    <div class="photo-gray" role="img" aria-label="Black and white kitchen with pale quartz island, farmhouse sink and pendant lamps"></div>
    <div class="page-number">02</div>
  </article>
</section>
<div class="spread-label spread-label--inside">Inside Page 1, 2</div>

</body>
</html>
```